In Home Personal IT Consultant (Nerd) Website and Logo QTgeek.net

Website and logo design for in home personal "nerd". Consulting services provided: Home Automation, Home Theater, Network and Wi-Fi installation, Computer Repair, and Virus Removal. Need simple site to promote QTgeek.net based in Santa Fe, New Mexico. You may choose to incorporate the Zia symbol from the New Mexico flag into the design, not mandatory. I am also a big fan of the movie Return of the Tinkers.
I have over 10 years of experience in the hospitality industry working with multi million dollar hotels and will apply that same level of service to the home. TechVara B+ and Shieldwise+ Certified. Available by appointment, primarily Evenings and Weekends. Consulting rate will be $70/hr.
Industry/Entity Type
Consulting
Number of Pages Required
1 page
Look and feel
Each slider illustrates characteristics of the customer's brand and the style your logo design should communicate.

```html
<!DOCTYPE html>
<html lang="en">
<head>
<meta charset="utf-8">
<title>Home IT Consulting — Services, Testimonials, Contact</title>
<link href="https://fonts.googleapis.com/css2?family=Open+Sans:wght@300;400;600;700&family=Roboto:wght@300;400&family=PT+Serif:ital@1&display=swap" rel="stylesheet">
<style>
:root{
  --teal:#1ec9d6;
  --teal-soft:#74cfd0;
  --teal-deep:#5aa8aa;
  --band-grey:#e9e9e9;
  --section-grey:#f3f3f3;
  --ink:#333;
  --body-grey:#5f5f5f;
  --footer:#131418;
  --footer-bar:#0e0f12;
  --footer-text:#8c8c8c;
  --white:#fff;
}
*{margin:0;padding:0;box-sizing:border-box}
html,body{width:1200px;height:1013px;overflow:hidden}
body{position:relative;font-family:"Roboto",sans-serif;background:var(--section-grey)}
.abs{position:absolute}

/* Services band */
.services{left:0;top:0;width:1200px;height:227px;background:var(--band-grey)}
.service-text{top:0;width:226px;height:136px;background:var(--white)}
.service-title{font-family:"Open Sans",sans-serif;font-weight:600;color:var(--teal);font-size:14.5px;line-height:13.5px}
.service-body{font-family:"Roboto",sans-serif;font-weight:300;color:var(--body-grey);font-size:11.3px;line-height:15px}
.read-more{font-family:"Open Sans",sans-serif;color:var(--teal);font-size:11.5px;display:flex;align-items:center;gap:5px}
.service-photo{top:0;width:225px;height:136px}
.notch{width:0;height:0;border-top:9px solid transparent;border-bottom:9px solid transparent}
.btn-services{left:492px;top:161px;width:217px;height:36px;background:var(--teal);color:var(--white);font-family:"Open Sans",sans-serif;font-weight:700;font-size:17px;display:flex;align-items:center;justify-content:center}

/* Testimonials */
.section-title{left:0;top:286px;width:1200px;text-align:center;font-family:"Open Sans",sans-serif;font-size:29px;color:var(--ink);font-weight:300;letter-spacing:-.2px}
.section-title strong{color:var(--teal);font-weight:700}
.testimonial{top:352px;width:286px;height:158px;background:var(--teal-soft)}
.quote-mark{position:absolute;width:30px;height:24px}
.quote-open{left:6px;top:26px}
.quote-close{right:5px;top:106px}
.testimonial p{position:absolute;left:40px;top:41px;width:236px;color:var(--white);font-family:"Open Sans",sans-serif;font-weight:300;font-size:11.8px;line-height:16px}
.testimonial cite{position:absolute;right:39px;top:110px;font-family:"PT Serif",serif;font-style:italic;color:#4f8e90;font-size:12.5px}
.avatar{width:55px;height:55px;border-radius:50%;border:3px solid var(--white);top:483px}
.pager{top:584px;width:26px;height:26px;background:#d3d3d3;display:flex;align-items:center;justify-content:center}

/* Footer */
.footer{left:0;top:659px;width:1200px;height:307px;background:var(--footer)}
.footer-bar{left:0;top:966px;width:1200px;height:47px;background:var(--footer-bar)}
.footer-title{top:722px;color:var(--white);font-family:"Open Sans",sans-serif;font-weight:600;font-size:14px}
.contact-item{left:150px;display:flex;align-items:center;gap:7px;color:var(--footer-text);font-size:11.5px;font-weight:300}
.contact-item svg{width:13px;height:13px}
.sitemap-item{left:430px;display:flex;align-items:center;gap:5px;color:var(--footer-text);font-size:11.5px;font-weight:300}
.sitemap-item::before{content:"";width:6px;height:6px;background:var(--teal-soft)}
.field{color:var(--white);font-size:11.3px;font-weight:300;border-bottom:1px solid #6b6d72;padding-bottom:3px}
.btn-send{left:962px;top:878px;width:89px;height:30px;background:var(--teal-soft);color:#111;font-size:16px;display:flex;align-items:center;justify-content:center}
.to-top{left:1139px;top:942px;width:43px;height:24px;background:#1b1c20;border-radius:4px 4px 0 0;display:flex;align-items:center;justify-content:center}
.copyright{left:0;top:981px;width:1300px;text-align:center;font-family:"Open Sans",sans-serif;color:#6f7074;font-size:11.5px;font-weight:300}
.copyright strong{font-weight:400;color:#8a8b8f}
.social{left:956px;top:982px;display:flex;gap:12px}
.social span{width:12px;height:12px;border-radius:50%;background:#5f6064}
</style>
</head>
<body>

<section class="abs services">
  <div class="abs service-text" style="left:150px">
    <h3 class="abs service-title" style="left:34px;top:7px">Network and<br>Wi-Fi installation</h3>
    <p class="abs service-body" style="left:36px;top:38px;width:185px">Donec a quam at ipsum luctus semper. Fusce sodales, tortor et porttitor aliquet, tortor</p>
    <a class="abs read-more" style="left:37px;top:98px">Read More <svg width="7" height="8" viewBox="0 0 7 8"><path d="M0 0L7 4L0 8Z" fill="#1ec9d6"/></svg></a>
  </div>
  <div class="abs service-photo" style="left:376px;background:linear-gradient(135deg,#d9d5cf,#b8ada1 45%,#3a3330)" role="img" aria-label="Technician mounting a wireless router on a wall"></div>
  <div class="abs notch" style="left:365px;top:47px;border-right:11px solid #cfcac3"></div>

  <div class="abs service-text" style="left:601px">
    <h3 class="abs service-title" style="left:33px;top:7px">Computer Repair</h3>
    <p class="abs service-body" style="left:36px;top:28px;width:165px">Donec a quam at ipsum luctus semper. Fusce sodales, tortor et porttitor aliquet, tortor sapien venenatis massa.</p>
    <a class="abs read-more" style="left:36px;top:98px">Read More <svg width="7" height="8" viewBox="0 0 7 8"><path d="M0 0L7 4L0 8Z" fill="#1ec9d6"/></svg></a>
  </div>
  <div class="abs service-photo" style="left:826px;width:226px;background:linear-gradient(120deg,#c8cdc6,#5b6a5c 45%,#2f9d62 80%,#48c47e)" role="img" aria-label="Close-up of a circuit board being repaired with tweezers"></div>
  <div class="abs notch" style="left:815px;top:47px;border-right:11px solid #9aa59a"></div>

  <a class="abs btn-services">View All Services</a>
</section>

<h2 class="abs section-title">CLIENT <strong>TESTIMONIALS</strong></h2>

<svg width="0" height="0" style="position:absolute">
  <defs>
    <g id="quote-open-shape"><path d="M0 24V12C0 4 4 0 12 0v5c-4 0-6 2-6 6h6v13zM18 24V12c0-8 4-12 12-12v5c-4 0-6 2-6 6h6v13z"/></g>
  </defs>
</svg>

<article class="abs testimonial" style="left:150px">
  <svg class="quote-mark quote-open" viewBox="0 0 30 24" fill="#5aa8aa"><use href="#quote-open-shape"/></svg>
  <p>Nulla commodo tellus non mauris mattis condimentum. Mauris feugiat lorem amet pharetra lacinia. Morbi tincidunt rhoncus posuere. Etiam at arcu in augue.</p>
  <cite>-Lorem ipsum</cite>
  <svg class="quote-mark quote-close" viewBox="0 0 30 24" fill="#5aa8aa"><use href="#quote-open-shape" transform="rotate(180 15 12)"/></svg>
</article>
<div class="abs avatar" style="left:150px;background:radial-gradient(circle at 50% 40%,#d9b8a0,#8a6a58 60%,#e8e8e8)" role="img" aria-label="Client portrait"></div>

<article class="abs testimonial" style="left:458px">
  <svg class="quote-mark quote-open" viewBox="0 0 30 24" fill="#5aa8aa"><use href="#quote-open-shape"/></svg>
  <p>Nulla commodo tellus non mauris mattis condimentum. Mauris feugiat lorem amet pharetra lacinia. Morbi tincidunt rhoncus posuere. Etiam at arcu in augue.</p>
  <cite>-Lorem ipsum</cite>
  <svg class="quote-mark quote-close" viewBox="0 0 30 24" fill="#5aa8aa"><use href="#quote-open-shape" transform="rotate(180 15 12)"/></svg>
</article>
<div class="abs avatar" style="left:457px;background:radial-gradient(circle at 50% 40%,#c9a893,#5a4a44 60%,#e5e5e5)" role="img" aria-label="Client portrait"></div>

<article class="abs testimonial" style="left:764px">
  <svg class="quote-mark quote-open" viewBox="0 0 30 24" fill="#5aa8aa"><use href="#quote-open-shape"/></svg>
  <p>Nulla commodo tellus non mauris mattis condimentum. Mauris feugiat lorem amet pharetra lacinia. Morbi tincidunt rhoncus posuere. Etiam at arcu in augue.</p>
  <cite>-Lorem ipsum</cite>
  <svg class="quote-mark quote-close" viewBox="0 0 30 24" fill="#5aa8aa"><use href="#quote-open-shape" transform="rotate(180 15 12)"/></svg>
</article>
<div class="abs avatar" style="left:764px;background:radial-gradient(circle at 50% 40%,#e2c0aa,#2b2424 60%,#f0f0f0)" role="img" aria-label="Client portrait"></div>

<a class="abs pager" style="left:572px" aria-label="Previous"><svg width="10" height="16" viewBox="0 0 10 16"><path d="M8 1L2 8L8 15" fill="none" stroke="#555" stroke-width="1.4"/></svg></a>
<a class="abs pager" style="left:603px" aria-label="Next"><svg width="10" height="16" viewBox="0 0 10 16"><path d="M2 1L8 8L2 15" fill="none" stroke="#555" stroke-width="1.4"/></svg></a>

<footer class="abs footer"></footer>
<div class="abs footer-bar"></div>

<h4 class="abs footer-title" style="left:151px">Contact Us</h4>
<div class="abs contact-item" style="top:756px"><svg viewBox="0 0 12 14"><path d="M6 0C3 0 1 2.2 1 5c0 3.5 5 9 5 9s5-5.5 5-9C11 2.2 9 0 6 0zm0 7a2 2 0 110-4 2 2 0 010 4z" fill="#74cfd0"/></svg>45 BC, making it over 2000</div>
<div class="abs contact-item" style="top:779px"><svg viewBox="0 0 14 14"><path d="M3 1l2 3-1.3 1.5c.8 1.8 2.2 3.2 4 4L9.3 8l3 2-1.2 2.6C6 12.5 1.5 8 1.3 3z" fill="#74cfd0"/></svg>01-555-246-810</div>
<div class="abs contact-item" style="top:801px"><svg viewBox="0 0 14 14"><rect x="1" y="3" width="12" height="8" fill="#74cfd0"/><path d="M1 3l6 5 6-5" fill="none" stroke="#131418" stroke-width="1"/></svg>info@byteworthhome.com</div>
<div class="abs contact-item" style="top:824px"><svg viewBox="0 0 14 14"><circle cx="7" cy="7" r="5.5" fill="none" stroke="#74cfd0"/><ellipse cx="7" cy="7" rx="2.5" ry="5.5" fill="none" stroke="#74cfd0"/><path d="M1.5 7h11" stroke="#74cfd0"/></svg>www.byteworthhome.com</div>

<h4 class="abs footer-title" style="left:428px">Sitemap</h4>
<div class="abs sitemap-item" style="top:756px">Home</div>
<div class="abs sitemap-item" style="top:780px">About</div>
<div class="abs sitemap-item" style="top:804px">Services</div>
<div class="abs sitemap-item" style="top:828px">Contact Us</div>

<h4 class="abs footer-title" style="left:602px">Get In Touch</h4>
<div class="abs field" style="left:602px;top:758px;width:216px">First Name :</div>
<div class="abs field" style="left:836px;top:758px;width:215px">Last Name :</div>
<div class="abs field" style="left:602px;top:794px;width:216px">Email:</div>
<div class="abs field" style="left:836px;top:794px;width:215px">Phone:</div>
<div class="abs field" style="left:602px;top:833px;width:449px;padding-bottom:5px">Comment:</div>
<a class="abs btn-send">SEND</a>

<a class="abs to-top" aria-label="Back to top"><svg width="18" height="10" viewBox="0 0 18 10"><path d="M1 9L9 1L17 9" fill="none" stroke="#fff" stroke-width="1.3"/></svg></a>

<p class="abs copyright">&copy; 2017 <strong>Byteworth Home Services</strong>. All Right Reserved.</p>
<div class="abs social" aria-label="Social links"><span></span><span></span><span></span><span></span></div>

</body>
</html>
```